Expanding Wealth Training Company Needs Training Program Brochures

We are expanding our range of courses and need to have attractive designs for 3 of the new courses we are launching.
Target Audience: Financial service professionals
Nationalities: Predominantly Asian
Courses:
1. Practical Estate Planning for Sales Growth - Level 1
2. Practical Protection Planning for Business Owners - Level 1
3. Practical Financial Counselling
The corporate color for the training company (Brightvale Institute) is RED. You can go to www.brightvaleinstitute.com.sg to see the colors. The current brochures are attached but please follow the write-ups in the separately attached Word files.

Target Market(s)

Financial Service Professionals (as known as financial planners)

Industry/Entity Type

Training

Requirements
Must have
• 1. Faces of professional people are work - either in a planning situation or counseling situation. Can have a mix of Western and Asian faces.
2. Limit to 2 pages (front and back) of a single sheet.

```html
<!DOCTYPE html>
<html lang="en">
<head>
<meta charset="utf-8">
<title>Practical Estate Planning for Sales Growth (Level 1)</title>
<link rel="stylesheet" href="https://fonts.googleapis.com/css2?family=Arimo:wght@400;700&display=swap">
<style>
  :root {
    --brand-red: #c8202f;
    --ink: #3a3a3a;
    --paper: #ffffff;
    --footer-bg: #ececec;
    --photo-warm: #d9a27a;
    --photo-deep: #8a5a3c;
    --photo-light: #f3dcc4;
  }
  * { box-sizing: border-box; margin: 0; padding: 0; }
  html, body { width: 849px; height: 1200px; overflow: hidden; background: var(--paper); }
  body { font-family: "Arimo", Arial, sans-serif; color: var(--ink); }
  .brochure { position: relative; width: 849px; height: 1200px; background: var(--paper); }

  .hero-photo {
    height: 258px;
    background: linear-gradient(135deg, var(--photo-light) 0%, var(--photo-warm) 45%, var(--photo-deep) 100%);
  }

  .course-title {
    margin: 22px 40px 0;
    text-align: center;
    color: var(--brand-red);
    font-weight: 700;
    font-size: 21px;
    white-space: nowrap;
  }
  .course-tagline {
    margin: 14px 40px 0;
    border: 1.5px solid var(--brand-red);
    padding: 7px 0;
    text-align: center;
    color: var(--brand-red);
    font-size: 16px;
  }
  .intro { margin: 18px 40px 0; font-size: 13px; line-height: 1.4; }
  .intro p + p { margin-top: 11px; }

  .objectives { margin: 16px 40px 0; }
  .objectives h2 {
    color: var(--brand-red);
    font-size: 14px;
    font-weight: 700;
    letter-spacing: 0.5px;
    padding-bottom: 4px;
    border-bottom: 1.5px solid var(--brand-red);
    margin-bottom: 6px;
  }
  .objective-columns { display: flex; gap: 24px; }
  .objective-list { flex: 1; list-style: none; font-size: 12px; line-height: 1.3; }
  .objective-list li { position: relative; padding-left: 14px; }
  .objective-list li::before {
    content: ""; position: absolute; left: 0; top: 5px;
    width: 6px; height: 6px; border-radius: 50%; background: var(--brand-red);
  }

  .footer-band {
    position: absolute; left: 0; right: 0; bottom: 0; top: 812px;
    background: var(--footer-bg);
    display: flex; padding: 22px 40px;
    gap: 40px;
  }
  .organisers { flex: 1; }
  .footer-label { color: var(--brand-red); font-weight: 700; font-size: 14px; }
  .organiser-marks { display: flex; align-items: center; gap: 30px; margin-top: 20px; }
  .org-name { display: flex; align-items: center; gap: 8px; font-size: 13px; font-weight: 700; color: var(--brand-red); }
  .org-dot { width: 30px; height: 30px; border-radius: 50%; background: var(--brand-red); flex: none; }
  .org-site { margin-top: 12px; font-size: 11px; }
  .award { flex: 1; font-size: 13px; line-height: 1.4; }
  .award p { margin-top: 6px; }
</style>
</head>
<body>
<main class="brochure">
  <div class="hero-photo" role="img" aria-label="Photograph of a smiling family of three relaxing together and reading a book"></div>

  <h1 class="course-title">PRACTICAL ESTATE PLANNING FOR SALES GROWTH (Level 1)</h1>
  <p class="course-tagline">A practical field-tested courseware for advanced market planning</p>

  <section class="intro">
    <p>As the clients go through their life journey from entering the job market and start with basic wealth protection through risk &amp; insurance planning, then progress to wealth accumulation through investment &amp; retirement planning, they will inevitably reach a point when thinking about wealth distribution through gift &amp; estate planning becomes necessary.</p>
    <p>The financial consultant therefore needs to equip himself/herself with this advanced market planning skills and knowledge to serve a growing need &ndash; especially when wealth planning has become increasingly complex. Apart from dealing with financial issues, the financial consultant today has to deal with social and legal/tax issues which may result from the choices his/her clients make as these (decisions) can impact how wealth is protected, preserved and distributed efficiently and effectively.</p>
    <p>This course is a practical, field-tested program that was specially designed to address the growing needs for such specialized skill. Since April 2007, more than 1,500 practitioners in the banking and financial services industry in Singapore, Malaysia and Indonesia have benefited from this program.</p>
  </section>

  <section class="objectives">
    <h2>OBJECTIVES</h2>
    <div class="objective-columns">
      <ul class="objective-list">
        <li>Understand how Estate Planning fits into a comprehensive Wealth Plan</li>
        <li>Recognize the Financial/Tax Aspects of Estate Planning (What you want to give)</li>
        <li>Understand the Social Aspects of Estate Planning (Who you want to give to)</li>
        <li>Appreciate the Legal Aspects of Estate Planning (When &amp; How you want to give)</li>
        <li>Learn the applications of Life Insurance in Estate Planning</li>
        <li>Learn Distribution Laws that affect Estate Planning (e.g. Wills Act, Intestate Succession, Section 49 L &amp; M of IA)</li>
      </ul>
      <ul class="objective-list">
        <li>Understand the applications of Trusts and other instruments relevant to Estate Planning</li>
        <li>Practice Presentation Scripts to open up opportunities to Affluent Market</li>
        <li>Learn how to ask the right questions for the right information to do planning</li>
        <li>Develop customised solutions for the unique needs of each client</li>
      </ul>
    </div>
  </section>

  <footer class="footer-band">
    <div class="organisers">
      <div class="footer-label">JOINTLY ORGANISED BY:</div>
      <div class="organiser-marks">
        <div class="org-name"><span class="org-dot"></span>Harbourline Practitioners Guild</div>
        <div class="org-name">Brightvale Institute</div>
      </div>
      <div class="org-site">www.brightvaleinstitute.com.sg</div>
    </div>
    <div class="award">
      <div class="footer-label">AWARD | CPD-Hours</div>
      <p>Participants who meet 75% class attendance are awarded a Certificate of Accomplishment. Financial services professionals get 18 CPD hours (50% knowledge, 50% skills) accreditation from Regional Insurance Practitioners Council (RIPC)</p>
    </div>
  </footer>
</main>
</body>
</html>
```